Exciting new vermouth brand needs a brilliant label!

We need a label design for an exciting new premium Italian Vermouth brand called Brunavera Vermouth.

Brunavera Vermouth is based on a recipe that has been handed down for four generations and is made in the traditional way in the Piedmonte region of Northern Italy.

Brunavera, which means 'heavenly' in Italian has been designed to elevate classic cocktails such as the Negroni, Americano and Manhattan with a base of Italian wine blended with botanicals such as wormwood, orange peel, rhubarb and cinchona. It has a delicately balanced bittersweet profile with hints of vanilla and citrus.

Its competitors include brands such as Vecchia Torre, Parelli and Danvelo (see the uploaded brief for more examples).

The label is for a 50cl dark bottle (please refer to the uploaded brief) and should be based on maximum dimensions of 70mm (width) x 110mm (height). There is no limit to embellishments such as foil printing, embossing or any other premium finishes. The label does not necessarily need to be rectangular.

Feedback will be given quickly and constructively after submissions to ensure that the process is as fair and useful as possible for everyone.

Target Market(s)

25-45 year old Europeans, 50:50 female:male

Industry/Entity Type

Wine / Spirits / Vermouth

Requirements
Must have
• Fantastic design that is distinct from competitors, a premium feel and great lettering.
Should not have
• Generic images or patterns that do not relate to the brand (Brunavera) or the product

```html
<!DOCTYPE html>
<html lang="en">
<head>
<meta charset="utf-8">
<title>Brunavera Vermouth Label</title>
<link rel="stylesheet" href="https://fonts.googleapis.com/css2?family=Bodoni+Moda:wght@500&family=Italiana&family=Montserrat:wght@500;600&display=swap">
<style>
  :root {
    --gold: #b99a52;
    --gold-light: #dcc583;
    --gold-dark: #977a35;
    --label-black: #060503;
    --art-tone: #2b2312;
    --page: #ffffff;
  }
  html, body {
    margin: 0;
    width: 1200px;
    height: 1200px;
    overflow: hidden;
    background: var(--page);
  }
  .label-canvas { display: block; width: 1200px; height: 1200px; }
  .brand-name {
    font-family: "Bodoni Moda", "Playfair Display", serif;
    font-weight: 500;
    font-size: 96px;
    fill: url(#goldSheen);
  }
  .product-name {
    font-family: "Italiana", "Didact Gothic", serif;
    font-size: 62px;
    fill: var(--gold);
  }
  .tagline {
    font-family: "Montserrat", sans-serif;
    font-weight: 600;
    font-size: 17px;
    letter-spacing: 3.4px;
    fill: var(--gold);
  }
  .descriptor, .volume {
    font-family: "Montserrat", sans-serif;
    font-weight: 500;
    font-size: 14px;
    fill: var(--gold);
  }
  .volume { font-size: 13px; }
  .frame-line { fill: none; stroke: var(--gold); stroke-width: 2.5; }
</style>
</head>
<body>
<svg class="label-canvas" viewBox="0 0 1200 1200" xmlns="http://www.w3.org/2000/svg">
  <defs>
    <linearGradient id="goldSheen" x1="0" y1="0" x2="1" y2="0">
      <stop offset="0" stop-color="var(--gold-light)"/>
      <stop offset="0.5" stop-color="var(--gold-dark)"/>
      <stop offset="1" stop-color="var(--gold-light)"/>
    </linearGradient>
    <radialGradient id="artGlow" cx="0.5" cy="0.45" r="0.6">
      <stop offset="0" stop-color="#4a3b1c"/>
      <stop offset="1" stop-color="var(--art-tone)"/>
    </radialGradient>
    <path id="brandArc" d="M165,382 Q390,262 615,382"/>
  </defs>

  <g class="label" transform="translate(210,4)">
    <!-- label body -->
    <path class="label-edge" fill="url(#goldSheen)"
          d="M105,1040 V340 C105,230 250,152 390,152 C530,152 675,230 675,340 V1040 Z"/>
    <path class="label-face" fill="var(--label-black)"
          d="M117,1028 V342 C117,240 255,165 390,165 C525,165 663,240 663,342 V1028 Z"/>

    <!-- inner frame -->
    <path class="frame-line" d="M147,1015 V360 C147,270 270,205 390,205 C510,205 633,270 633,360 V1015 Z"/>
    <line class="frame-line" x1="300" y1="232" x2="480" y2="232"/>
    <line class="frame-line" x1="180" y1="465" x2="180" y2="665"/>
    <line class="frame-line" x1="600" y1="465" x2="600" y2="665"/>

    <!-- brand name -->
    <text class="brand-name" text-anchor="middle">
      <textPath href="#brandArc" startOffset="50%" textLength="430" lengthAdjust="spacingAndGlyphs">BRUNAVERA</textPath>
    </text>

    <!-- emblem area -->
    <rect class="emblem-art" role="img" aria-label="Gold line illustration of a winged figure with small four-point stars"
          x="240" y="370" width="300" height="310" rx="16" fill="url(#artGlow)"/>

    <!-- product band -->
    <path class="frame-line" d="M172,1000 V685 H608 V1000"/>
    <line class="frame-line" x1="172" y1="800" x2="608" y2="800"/>
    <rect class="frame-line" x="194" y="705" width="392" height="75"/>
    <text class="product-name" x="390" y="766" text-anchor="middle" textLength="320" lengthAdjust="spacingAndGlyphs">VERMOUTH</text>

    <rect class="star-mark" role="img" aria-label="Small gold star" x="318" y="818" width="24" height="24" rx="4" fill="var(--art-tone)"/>
    <rect class="star-mark" role="img" aria-label="Small gold star" x="438" y="818" width="24" height="24" rx="4" fill="var(--art-tone)"/>

    <!-- details box -->
    <path class="frame-line" d="M355,975 H203 V852 H578 V975 H425"/>
    <text class="tagline" x="390" y="894" text-anchor="middle">PREMIUM ITALIAN</text>
    <text class="descriptor" x="390" y="928" text-anchor="middle">WINE BLENDED</text>
    <text class="descriptor" x="390" y="947" text-anchor="middle">WITH BOTANICALS</text>
    <text class="volume" x="390" y="980" text-anchor="middle">500ML</text>
  </g>
</svg>
</body>
</html>
```